Hollywood cinema lovers club for our cinema
Tavis Reelhouse is a multiplex (cinema) located in central India where mostly Hindi (Bollywood) films are popular. The management wants to create a campaign to attract and to generate a database of English (Hollywood) film lovers.
The campaign is proposed to be named as “Hello Hollywood”.
The poster/ display design is desired for 6’ x 4’ poster size.
Also the same design to be used for in audi display in 720dpi.

Target Market(s)

Movie goers and prospective movie goers

Industry/Entity Type

Club

Requirements
Must have
• Evident linkage to Hollywood and Tavis Reelhouse and English
Should not have
• No obscenity
no-smoking scenes
no nudity

```html
<!DOCTYPE html>
<html lang="en">
<head>
<meta charset="utf-8">
<title>Hello Hollywood – Tavis Reelhouse</title>
<link rel="stylesheet" href="https://fonts.googleapis.com/css2?family=Luckiest+Guy&family=Nunito:wght@600&display=swap">
<style>
  :root {
    --bar-black: #000000;
    --stage-deep: #0714a8;
    --stage-mid: #1b36ee;
    --stage-bright: #2f5cff;
    --spot-cyan: rgba(120, 225, 255, 0.85);
    --title-fill: #6fd2ff;
    --title-core: #3aa0f5;
    --title-edge: #ffffff;
    --title-halo: #2fb4ff;
    --band-tint: rgba(140, 160, 255, 0.38);
    --brand-white: #ffffff;
  }
  html, body {
    margin: 0;
    padding: 0;
    width: 1200px;
    height: 800px;
    overflow: hidden;
    background: var(--bar-black);
  }
  .poster {
    position: relative;
    width: 1200px;
    height: 800px;
    background: var(--bar-black);
    overflow: hidden;
  }
  .red-carpet-scene {
    position: absolute;
    left: 0;
    top: 78px;
    width: 1200px;
    height: 640px;
    background:
      radial-gradient(ellipse 150px 90px at 60px 40px, var(--spot-cyan), transparent 70%),
      radial-gradient(ellipse 150px 90px at 1140px 40px, var(--spot-cyan), transparent 70%),
      radial-gradient(ellipse 90px 60px at 300px 70px, rgba(120, 225, 255, 0.5), transparent 70%),
      radial-gradient(ellipse 90px 60px at 900px 70px, rgba(120, 225, 255, 0.5), transparent 70%),
      radial-gradient(ellipse 70px 50px at 470px 50px, rgba(120, 225, 255, 0.4), transparent 70%),
      radial-gradient(ellipse 70px 50px at 730px 50px, rgba(120, 225, 255, 0.4), transparent 70%),
      radial-gradient(ellipse 160px 60px at 200px 600px, rgba(100, 200, 255, 0.45), transparent 70%),
      radial-gradient(ellipse 160px 60px at 1010px 600px, rgba(100, 200, 255, 0.45), transparent 70%),
      radial-gradient(ellipse 220px 260px at 600px 330px, rgba(90, 170, 255, 0.5), transparent 75%),
      linear-gradient(180deg, var(--stage-deep) 0%, var(--stage-bright) 45%, var(--stage-mid) 75%, var(--stage-deep) 100%);
    box-shadow: inset 0 0 110px 40px rgba(0, 0, 0, 0.9);
  }
  .title-art {
    position: absolute;
    left: 0;
    top: 0;
    width: 1200px;
    height: 800px;
    z-index: 2;
  }
  .campaign-title {
    font-family: "Luckiest Guy", "Arial Black", sans-serif;
    font-size: 128px;
    fill: url(#titleFill);
    stroke: var(--title-edge);
    stroke-width: 9px;
    stroke-linejoin: round;
    paint-order: stroke fill;
    filter: drop-shadow(0 0 14px var(--title-halo));
  }
  .brand-band {
    position: absolute;
    left: 0;
    top: 552px;
    width: 1200px;
    height: 116px;
    background: var(--band-tint);
    display: flex;
    align-items: center;
    justify-content: center;
    z-index: 3;
  }
  .brand-name {
    font-family: "Nunito", "Helvetica", sans-serif;
    font-weight: 600;
    font-size: 88px;
    color: var(--brand-white);
    letter-spacing: -1px;
    margin-top: -8px;
  }
  .letterbox {
    position: absolute;
    left: 0;
    width: 1200px;
    background: var(--bar-black);
    z-index: 4;
  }
  .letterbox--top { top: 0; height: 78px; }
  .letterbox--bottom { bottom: 0; height: 82px; }
</style>
</head>
<body>
  <main class="poster">
    <div class="red-carpet-scene" role="img" aria-label="Blue-lit red carpet with rope stanchions, spotlights and press photographers"></div>
    <svg class="title-art" viewBox="0 0 1200 800" aria-labelledby="campaignTitle">
      <defs>
        <linearGradient id="titleFill" x1="0" y1="0" x2="0" y2="1">
          <stop offset="0" stop-color="#a8ecff"/>
          <stop offset="0.55" stop-color="#6fd2ff"/>
          <stop offset="1" stop-color="#3aa0f5"/>
        </linearGradient>
      </defs>
      <text id="campaignTitle" class="campaign-title" x="42" y="308" textLength="1116" lengthAdjust="spacingAndGlyphs">“HELLO HOLLYWOOD!”</text>
    </svg>
    <div class="brand-band">
      <span class="brand-name">Tavis Reelhouse</span>
    </div>
    <div class="letterbox letterbox--top"></div>
    <div class="letterbox letterbox--bottom"></div>
  </main>
</body>
</html>
```